Design a simple and clean PowerPoint slide templates for a Board meeting. The slides should have predominantly white backgrounds and use the brand graphic standards (attached). I'm also attached a PowerPoint master that I don't like, as it's too basic.
The company name is Harborline Weighworks.
It sells, calibrates, services and repairs industrial and commercial scales of all types. In particular, Truck scales, floor scales, counting scales and benchtop scales.
The website is harborlineweighworks.example but this are the old colors, so ignore the logo and colors. We are launching a new logo and new look. Several variations of the logo are available.

```html
<!DOCTYPE html>
<html lang="en">
<head>
<meta charset="utf-8">
<title>Harborline Weighworks – Board Slide Templates, Concept 01</title>
<link rel="stylesheet" href="https://fonts.googleapis.com/css2?family=Russo+One&family=Inter:wght@400;500;600;700&display=swap">
<style>
  :root{
    --navy:#1b2f5a;
    --navy-text:#0f2a55;
    --orange:#f7941d;
    --orange-soft:#fbc78c;
    --orange-pale:#fbe8d3;
    --grey:#5f5f5f;
    --body:#555a62;
    --white:#ffffff;
    --bg-top:#01305f;
    --bg-bottom:#02112a;
  }
  *{box-sizing:border-box;margin:0;padding:0}
  html,body{width:749px;height:1200px;overflow:hidden}
  body{
    position:relative;
    background:linear-gradient(180deg,var(--bg-top) 0%,#012247 50%,var(--bg-bottom) 100%);
    font-family:"Inter",Arial,sans-serif;
  }
  .display{font-family:"Russo One","Arial Black",sans-serif;font-weight:400}

  .concept-title{position:absolute;left:100px;top:48px;color:var(--white);font-size:36px;letter-spacing:.5px}
  .concept-fonts{position:absolute;left:100px;top:92px;color:var(--white);font-size:16.5px;font-weight:500;letter-spacing:-.3px}

  .slide{position:absolute;background:var(--white);overflow:hidden;box-shadow:0 6px 14px rgba(0,0,0,.35)}
  .slide::before{content:"";position:absolute;left:0;top:0;bottom:0;width:10px;background:var(--orange)}
  .slide.small::before{width:5px}

  .brand{position:absolute;display:flex;align-items:center;gap:8px}
  .brand-square{width:20px;height:20px;background:var(--orange)}
  .brand-name{font-family:"Russo One","Arial Black",sans-serif;color:var(--navy);font-size:15.5px;line-height:16px;letter-spacing:1px;text-transform:uppercase}

  .deco-shape{position:absolute;border-radius:50%}

  /* title slide */
  .cover{left:101px;top:125px;width:543px;height:305px}
  .cover .brand{left:50px;top:32px}
  .cover-title{position:absolute;left:50px;top:130px;color:var(--orange);font-size:32px;letter-spacing:.3px}
  .cover-rule{position:absolute;left:50px;top:172px;width:62px;height:2px;background:var(--orange)}
  .cover-tagline{position:absolute;left:50px;top:182px;color:var(--grey);font-size:12px;font-weight:600;letter-spacing:-.2px}
  .cover-url{position:absolute;left:50px;top:276px;color:var(--orange);font-size:8.5px}
  .cover .deco-shape{left:336px;top:40px;width:185px;height:185px;background:var(--orange-soft)}

  /* content slides */
  .small{width:261px;height:147px}
  .s2{left:101px;top:461px}
  .s3{left:383px;top:461px}
  .s4{left:101px;top:630px}
  .s5{left:383px;top:630px}
  .slide-heading{position:absolute;left:20px;top:15px;color:var(--navy-text);font-size:8.6px}
  .heading-rule{position:absolute;left:20px;top:28px;width:29px;height:1px;background:var(--orange)}
  .intro{position:absolute;left:20px;right:16px;top:39px;color:var(--navy-text);font-size:4.4px;line-height:7px;font-weight:600}
  .columns{position:absolute;left:20px;right:24px;display:flex;gap:11px}
  .columns .col{flex:1}
  .sub{color:var(--orange);font-size:4.2px;font-weight:700;line-height:7px}
  .copy{color:var(--body);font-size:4.1px;line-height:7.4px;text-align:justify}
  .single{position:absolute;left:20px;right:18px;top:39px}
  .single .copy + .copy{margin-top:7.4px}
  .footer{position:absolute;left:20px;right:12px;bottom:9px;display:flex;align-items:center;gap:5px}
  .footer-url{color:var(--orange);font-size:3.9px;font-family:"Russo One",Arial,sans-serif;letter-spacing:.2px}
  .footer-line{flex:1;height:.6px;background:var(--orange)}
  .footer-page{color:var(--orange);font-size:4px;font-weight:600}

  /* closing slide */
  .closing{left:101px;top:798px;width:543px;height:306px}
  .closing .deco-shape{left:75px;top:35px;width:180px;height:180px;background:var(--orange-pale)}
  .closing .brand{left:50px;top:134px}
  .thanks{position:absolute;left:325px;top:100px;color:var(--orange);font-size:50px;line-height:54px;letter-spacing:-.5px}
</style>
</head>
<body>
  <h1 class="concept-title display">Concept 01</h1>
  <p class="concept-fonts">Fonts used: Keelson Sans &amp; Tidewell</p>

  <section class="slide cover">
    <div class="brand"><span class="brand-square"></span><span class="brand-name">Harborline<br>Weighworks</span></div>
    <h2 class="cover-title display">Our Powerpoint</h2>
    <div class="cover-rule"></div>
    <p class="cover-tagline">Measured Right. Trusted Every Load.</p>
    <p class="cover-url display">harborlineweighworks.example</p>
    <div class="deco-shape" aria-hidden="true"></div>
  </section>

  <section class="slide small s2">
    <h3 class="slide-heading display">Two Column with Heading</h3>
    <div class="heading-rule"></div>
    <p class="intro">Quarterly review of service operations, calibration volumes and truck scale installations across all regional branches this period.</p>
    <div class="columns" style="top:62px">
      <div class="col"><p class="sub">Service highlights this quarter</p><p class="copy">Field teams completed scheduled calibrations for floor, counting and benchtop scales on time, while repair turnaround improved across every branch and customer renewals rose steadily.</p></div>
      <div class="col"><p class="sub">Calibration outlook and priorities</p><p class="copy">Field teams completed scheduled calibrations for floor, counting and benchtop scales on time, while repair turnaround improved across every branch and customer renewals rose steadily.</p></div>
    </div>
    <div class="footer"><span class="footer-url">harborlineweighworks.example</span><span class="footer-line"></span><span class="footer-page">2</span></div>
  </section>

  <section class="slide small s3">
    <h3 class="slide-heading display">Two Column</h3>
    <div class="heading-rule"></div>
    <p class="intro">Quarterly review of service operations, calibration volumes and truck scale installations across all regional branches this period.</p>
    <div class="columns" style="top:62px">
      <div class="col"><p class="copy">Field teams completed scheduled calibrations for floor, counting and benchtop scales on time, while repair turnaround improved across every branch and customer renewals rose steadily.</p></div>
      <div class="col"><p class="copy">Field teams completed scheduled calibrations for floor, counting and benchtop scales on time, while repair turnaround improved across every branch and customer renewals rose steadily.</p></div>
    </div>
    <div class="footer"><span class="footer-url">harborlineweighworks.example</span><span class="footer-line"></span><span class="footer-page">3</span></div>
  </section>

  <section class="slide small s4">
    <h3 class="slide-heading display">Two Column Plain</h3>
    <div class="heading-rule"></div>
    <div class="columns" style="top:39px">
      <div class="col"><p class="copy">Field teams completed scheduled calibrations for floor, counting and benchtop scales on time, while repair turnaround improved across every branch and customer renewals rose steadily.</p></div>
      <div class="col"><p class="copy">Field teams completed scheduled calibrations for floor, counting and benchtop scales on time, while repair turnaround improved across every branch and customer renewals rose steadily.</p></div>
    </div>
    <div class="footer"><span class="footer-url">harborlineweighworks.example</span><span class="footer-line"></span><span class="footer-page">4</span></div>
  </section>

  <section class="slide small s5">
    <h3 class="slide-heading display">Column</h3>
    <div class="heading-rule"></div>
    <div class="single">
      <p class="copy">Field teams completed scheduled calibrations for floor, counting and benchtop scales on time, while repair turnaround improved across every branch and customer renewals rose steadily.</p>
      <p class="copy">Quarterly review of service operations, calibration volumes and truck scale installations across all regional branches this period.</p>
      <p class="copy">Next steps include expanding truck scale capacity, training new technicians and reviewing pricing for long term service agreements.</p>
    </div>
    <div class="footer"><span class="footer-url">harborlineweighworks.example</span><span class="footer-line"></span><span class="footer-page">5</span></div>
  </section>

  <section class="slide closing">
    <div class="deco-shape" aria-hidden="true"></div>
    <div class="brand"><span class="brand-square"></span><span class="brand-name">Harborline<br>Weighworks</span></div>
    <p class="thanks display">THANK<br>YOU.</p>
  </section>
</body>
</html>
```